Fitness Centre/Personal Trainer Business Card

We need a business card design for a company based in Singapore called 'Vigor Summit'.

We are a team of Personal Trainers and we are planning to open our new training facility.

This design will also be printed/painted on the walls in our gym.

We are a new breed of personal trainers who take fitness seriously and holistically. We do not merely train our clients to be big and muscular.

We believe in wholeness. In our opinion, fitness should include: strength, speed, flexibility, mobility, stamina & agility. These are what we train for. Of course, nutrition/diet is key.

We use fitness tools such as kettlebells, QLV, Pylometric boxes, battling ropes, clubbells, medicine balls, bulgarian bags etc - functional and non-bulky tools.

I currently have a Facebook page 'Vigor Summit SG' which shows a logo of a kettlebell. But my business focus has since changed.

Services provided:
- Kettlebell Sport Preparation
- Calisthenics Training
- Corrective Exercises
- Sports Strength & Conditioning
- 28 days Weight Loss Program
- Myofascial Rehab Therapy
- Sports/Thai Massage

Main colors for the design should be BLACK & YELLOW. We envision a design which is able to protray the holistic view we take on fitness. Also it should somewhat appeal to the ladies and not intimidate them.

Target Market(s)

People between 18-35 years old. Students and working class alike.

Industry/Entity Type

Training

Requirements
Must have
• Name: Marcus Oleander Pryce
Fitness Coach
Corrective Exercise Specialist
M: +65 9372 6058
E: marcus@sgvigorsummit-example.com

Double-sided please.
Nice to have
• "What is your vigor summit?"

```html
<!DOCTYPE html>
<html lang="en">
<head>
<meta charset="utf-8">
<title>Vigor Summit Business Card</title>
<link rel="stylesheet" href="https://fonts.googleapis.com/css2?family=Archivo+Black&family=Play:wght@400;700&display=swap">
<style>
  :root {
    --stage: #e9e9ea;
    --ink: #111111;
    --card-black: #141414;
    --card-black-tone: #2a2a2a;
    --card-yellow: #f4ea1c;
    --card-yellow-tone: #e2d81a;
    --accent-yellow: #f2e600;
  }
  * { box-sizing: border-box; margin: 0; padding: 0; }
  html, body { width: 1200px; height: 861px; overflow: hidden; }
  body {
    background: var(--stage);
    font-family: "Play", "Arial", sans-serif;
    position: relative;
  }
  .card {
    position: absolute;
    top: 276px;
    width: 540px;
    height: 309px;
    border-radius: 16px;
    overflow: hidden;
    box-shadow: 0 10px 30px rgba(0,0,0,0.18);
  }
  .card--front { left: 40px; background: var(--card-black); }
  .card--back { left: 620px; background: var(--card-yellow); }

  .texture {
    position: absolute;
    inset: 0;
  }
  .card--front .texture {
    background: linear-gradient(160deg, var(--card-black-tone) 0%, var(--card-black) 55%, var(--card-black-tone) 100%);
  }
  .card--back .texture {
    background: linear-gradient(160deg, var(--card-yellow-tone) 0%, var(--card-yellow) 55%, var(--card-yellow-tone) 100%);
  }

  .tagline {
    position: absolute;
    left: 48px;
    top: 188px;
    font-size: 31px;
    line-height: 1.1;
    color: var(--accent-yellow);
    white-space: nowrap;
  }

  .brand-name {
    position: absolute;
    left: 42px;
    top: 44px;
    font-family: "Archivo Black", "Arial Black", sans-serif;
    font-weight: 400;
    font-size: 44px;
    line-height: 1;
    color: var(--ink);
    white-space: nowrap;
  }

  .contact-block {
    position: absolute;
    right: 38px;
    top: 172px;
    text-align: right;
    color: var(--ink);
  }
  .person-name {
    font-family: "Archivo Black", "Arial Black", sans-serif;
    font-size: 23px;
    line-height: 1.1;
    letter-spacing: 0.5px;
    white-space: nowrap;
  }
  .person-role {
    font-size: 14px;
    font-weight: 700;
    line-height: 1.2;
    margin-top: 5px;
    white-space: nowrap;
  }
  .contact-list { margin-top: 20px; }
  .contact-line {
    display: flex;
    justify-content: flex-end;
    align-items: center;
    gap: 6px;
    font-size: 14px;
    line-height: 1.2;
    white-space: nowrap;
  }
  .contact-line + .contact-line { margin-top: 9px; }
  .contact-line svg { width: 16px; height: 16px; flex: none; }
</style>
</head>
<body>

<section class="card card--front" aria-label="Card front">
  <div class="texture" role="img" aria-label="Background of faint motivational words in dark grey tones"></div>
  <p class="tagline">What is your vigor summit?</p>
</section>

<section class="card card--back" aria-label="Card back">
  <div class="texture" role="img" aria-label="Background of faint motivational words in darker yellow tones"></div>

  <h1 class="brand-name">VIGOR SUMMIT</h1>

  <div class="contact-block">
    <p class="person-name">MARCUS OLEANDER PRYCE</p>
    <p class="person-role">Fitness Coach/ Corrective Exercise Specialist</p>
    <div class="contact-list">
      <p class="contact-line">+65 9372 6058
        <svg viewBox="0 0 16 16" aria-hidden="true"><circle cx="8" cy="8" r="8" fill="#111"/><path d="M5.5 4.2l1.4 1.9-.9 1a5 5 0 0 0 2.9 2.9l1-.9 1.9 1.4-.8 1.4c-3.4-.3-6-2.9-6.3-6.3z" fill="#f4ea1c"/></svg>
      </p>
      <p class="contact-line">marcus@sgvigorsummit-example.com
        <svg viewBox="0 0 16 16" aria-hidden="true"><circle cx="8" cy="8" r="8" fill="#111"/><rect x="4" y="5.2" width="8" height="5.6" rx="0.6" fill="#f4ea1c"/><path d="M4.3 5.6L8 8.4l3.7-2.8" fill="none" stroke="#111" stroke-width="0.9"/></svg>
      </p>
    </div>
  </div>
</section>

</body>
</html>
```